Design mobile friendly real estate and property management company landing page

Design a clean, crisp modern looking landing page that is mobile-friendly (must resize, preferably using bootstrap framework). Landing page will consist of heading with login area, company info, body consists of company description and services, a list of available rental properties with photos, and a footer with additional links and info. Working on updating with text for text areas marked A, B, and C on the layout pdf, but in meantime, lorem ipsum is fine. I can connect events to most buttons, etc. Just need the bootstrap and html functionality set up. Previous company website (which should not be relied upon) is www.qlbt.net This is somewhat of a template for a start, but looking for a more professional and modern design for the new website. But this gives an idea of the content and what needs to be displayed, and how.

Target Market(s)

Clients looking for a property management company that is efficient and well-organized.

Industry/Entity Type

Property Management

Coding

Coded - Design and coding required

Number of Pages Required

1 page

Font styles to use
Sans Serif

Colors
0355a3

Requirements
Must have
• Resize for the screen using bootstrap.
• Navigation that collapses for mobile devices
• Large text boxes and good solid spacing around all elements.
Nice to have
• for property images it would be nice if they can be swiped on touch enabled devices (to the next or previous image). And have navigation that can be clicked to next or previous images.
• Would be nice if a captcha verification was included on contact form.
Should not have
• Fancy or eccentric art

```html
<!DOCTYPE html>
<html lang="en">
<head>
<meta charset="utf-8">
<title>Northgate Realty Services</title>
<link rel="stylesheet" href="https://fonts.googleapis.com/css2?family=Cinzel:wght@400;500;600;700&family=Open+Sans:ital,wght@0,400;0,600;0,700;1,400&family=Raleway:wght@400;500&family=Lato:wght@400;700&display=swap">
<style>
:root{
  --brand:#0355a3;
  --brand-dark:#01407d;
  --ink:#111;
  --text:#333;
  --muted:#666;
  --rule:#d6d6d6;
  --light:#efefef;
  --footer:#2b2b2b;
  --footer-text:#d8d8d8;
  --white:#fff;
}
*{box-sizing:border-box;margin:0;padding:0}
html,body{width:1200px;height:2765px;overflow:hidden}
body{font-family:"Open Sans",Arial,sans-serif;color:var(--text);background:var(--white);position:relative}
.wrap{width:1040px;margin:0 auto;position:relative}
svg{display:block}

/* top bar */
.topbar{height:37px;background:#000;color:var(--white);font-size:15px}
.topbar .wrap{display:flex;align-items:center;height:37px;gap:34px}
.topbar .item{display:flex;align-items:center;gap:10px}
.login{position:absolute;right:0;top:0;height:37px;width:96px;background:var(--brand);display:flex;align-items:center;justify-content:center;gap:8px;font-weight:600}

/* header */
.header{height:113px}
.header .wrap{height:113px}
.brand{position:absolute;left:0;top:20px;width:360px;text-align:center}
.brand .name{font-family:"Cinzel",serif;font-size:30px;font-weight:500;color:var(--ink);line-height:1;white-space:nowrap}
.brand .sub{font-family:"Cinzel",serif;font-size:18px;font-weight:500;letter-spacing:7px;color:var(--ink);line-height:1;margin-top:12px;display:flex;align-items:center;justify-content:center;gap:10px;white-space:nowrap}
.brand .sub::before,.brand .sub::after{content:"";width:84px;height:1px;background:var(--ink)}
.weather{position:absolute;right:0;top:16px;width:346px;height:82px;border:1px solid #ccc;background:#f6f6f6;overflow:hidden}
.weather .title{font-size:15px;font-weight:700;color:#444;padding:4px 8px;font-family:Arial,sans-serif}
.weather .today{position:absolute;left:8px;top:30px;display:flex;align-items:center;gap:6px}
.weather .temp{font-size:34px;color:#888;font-weight:700;line-height:1}
.weather .lbl{font-size:11px;color:#555;line-height:1.2}
.weather .days{position:absolute;left:176px;top:28px;display:flex;gap:4px}
.weather .day{font-size:8px;line-height:10px;color:#666;text-align:center;width:38px}
.weather .day svg{margin:0 auto 2px}

/* nav */
.nav{height:45px;background:var(--brand)}
.nav ul{list-style:none;display:flex;height:45px}
.nav li{flex:1;text-align:center;line-height:45px;font-family:"Cinzel",serif;font-size:15px;color:var(--white);letter-spacing:1px;border-right:1px solid rgba(255,255,255,.35);white-space:nowrap}
.nav li:last-child{border-right:0}
.nav li.active{background:#0a0a0a;flex:0 0 100px}

/* hero */
.hero{height:470px;position:relative;background:linear-gradient(180deg,#9ab4cf 0%,#c7c2b7 50%,#6d6a67 100%)}
.hero .caption{position:absolute;left:0;right:0;bottom:0;height:94px;background:rgba(0,0,0,.55);color:var(--white);font-family:"Raleway",sans-serif;font-size:26px;text-align:center;line-height:34px;padding-top:12px}
.arrow-tab{position:absolute;top:195px;width:44px;height:44px;background:rgba(255,255,255,.8);display:flex;align-items:center;justify-content:center}
.arrow-tab.left{left:0}.arrow-tab.right{right:0}

/* section titles */
.section-title{font-family:"Cinzel",serif;font-size:37px;text-align:center;color:var(--ink);letter-spacing:1px;font-weight:500;white-space:nowrap}
.divider{width:272px;height:20px;margin:14px auto 0;position:relative}
.divider::before{content:"";position:absolute;left:0;right:0;top:10px;height:1px;background:var(--rule)}
.divider svg{position:absolute;left:126px;top:0}

/* welcome */
.welcome{height:428px;padding-top:50px}
.welcome p{font-size:13px;line-height:24px;text-align:center;color:#222;margin-top:22px;padding:0 2px}
.welcome p a{color:var(--brand);text-decoration:none}
.callbox{margin:62px auto 0;width:710px;height:70px;border:1px solid #ccc;border-radius:8px;background:linear-gradient(#fff,#ececec);display:flex;align-items:center;padding-left:22px;gap:18px;font-family:"Lato",sans-serif;font-size:31px;color:#111;position:relative;white-space:nowrap}
.callbox::before{content:"";position:absolute;left:74px;top:-12px;border:11px solid transparent;border-top:0;border-bottom:12px solid #ccc}
.callbox strong{color:var(--brand);font-weight:700}

/* services */
.services{height:417px;background:var(--brand);padding-top:43px;color:var(--white)}
.services .section-title{color:var(--white)}
.services .divider::before{background:rgba(255,255,255,.3)}
.service-row{display:flex;justify-content:space-between;margin:48px 0 0;padding:0 20px}
.service{width:240px;text-align:center}
.service .icon{width:103px;height:103px;margin:0 auto;border-radius:50%;background:#111;border:3px solid var(--white);display:flex;align-items:center;justify-content:center}
.service h3{font-family:"Cinzel",serif;font-size:19px;line-height:24px;margin-top:20px;font-weight:600;letter-spacing:1px}
.service p{font-size:12px;line-height:18px;margin-top:6px}
.service .plus{width:16px;height:16px;margin:12px auto 0;background:#000;color:#fff;font-size:14px;line-height:15px;font-weight:700}
.svc-arrow{position:absolute;top:318px;font-size:26px;color:#fff}

/* featured */
.featured{height:525px;padding-top:48px}
.cards{display:flex;justify-content:space-between;margin-top:28px}
.card{width:241px;height:303px;border:2px solid #ddd;background:#fff;position:relative}
.card .photo{margin:8px;height:133px}
.card h4{font-family:"Cinzel",serif;font-size:15px;font-weight:600;color:#222;padding:0 10px;margin-top:12px;letter-spacing:.3px;white-space:nowrap}
.card .desc{font-size:11.5px;color:#777;padding:0 10px;margin-top:4px;white-space:nowrap;overflow:hidden}
.card .tag{position:absolute;left:10px;top:220px;background:#0a0a0a;color:#fff;font-size:12px;font-weight:600;padding:5px 10px}
.card .price{position:absolute;right:10px;top:214px;font-size:23px;font-weight:700;color:#111}
.card .stats{position:absolute;left:0;right:0;bottom:0;height:42px;border-top:1px solid #ddd;display:flex}
.card .stat{flex:1;font-size:10px;color:#555;display:flex;align-items:center;justify-content:center;gap:5px;border-right:1px solid #ddd;white-space:nowrap}
.card .stat:last-child{border-right:0}

/* testimonials */
.testimonials{height:295px;background:var(--light);padding-top:45px}
.quote{display:flex;margin-top:26px;gap:36px;position:relative}
.avatar{width:84px;height:84px;border-radius:50%;border:3px solid var(--brand);flex:none;background:radial-gradient(circle at 50% 40%,#d9b9a0,#6f7d8c)}
.quote p{font-style:italic;font-size:12.5px;line-height:21px;color:#222;padding-top:2px}
.quote .who{font-size:14px;font-weight:700;color:#222;margin-top:12px}
.quote .nav-arrows{position:absolute;right:0;top:100px;font-size:20px;color:#222;letter-spacing:10px;font-weight:700}
.quote .rule{position:absolute;left:120px;right:0;top:130px;height:1px;background:#ccc}

/* newsletter */
.newsletter{height:98px;background:linear-gradient(180deg,#0b63b8,var(--brand-dark))}
.newsletter .wrap{height:98px}
.newsletter .circle{position:absolute;left:0;top:26px;width:46px;height:46px;border-radius:50%;border:2px solid #fff;background:#111;display:flex;align-items:center;justify-content:center}
.newsletter h2{position:absolute;left:71px;top:32px;font-family:"Cinzel",serif;color:#fff;font-weight:500;font-size:25px;line-height:32px;letter-spacing:1.5px;white-space:nowrap}
.newsletter .chev{position:absolute;left:376px;top:34px}
.newsletter .input{position:absolute;left:419px;top:28px;width:450px;height:41px;background:#fff;font-size:13px;color:#222;padding:11px 12px}
.newsletter .btn{position:absolute;left:887px;top:28px;width:153px;height:41px;background:#000;color:#fff;font-weight:700;font-size:17px;text-align:center;line-height:41px}

/* footer */
.footer{height:292px;background:var(--footer);color:var(--footer-text);padding-top:18px}
.footer .wrap{display:flex}
.fcol h5{font-family:"Cinzel",serif;font-size:18px;color:#fff;font-weight:500;letter-spacing:1px;padding-bottom:10px;border-bottom:1px solid #444;margin-bottom:12px;white-space:nowrap}
.fcol ul{list-style:none;font-size:12px;line-height:26.5px}
.fcol li::before{content:"›";margin-right:10px;color:#aaa}
.col-nav{width:160px}.col-links{width:170px;margin-left:68px}.col-form{width:265px;margin-left:65px}.col-touch{width:244px;margin-left:68px}
.field{background:#fff;color:#222;font-size:12px;height:32px;padding:8px 10px;margin-bottom:8px;width:265px}
.field.msg{height:62px}
.submit{display:inline-block;background:var(--brand);color:#fff;font-weight:700;font-size:14px;padding:6px 12px;margin-top:4px}
.touch{display:flex;gap:18px;font-size:12px;line-height:20px;margin-bottom:22px;align-items:center}
.touch .ic{width:30px;height:30px;background:var(--brand);display:flex;align-items:center;justify-content:center;flex:none}
.touch b{color:#fff}
.copyright{height:45px;background:var(--brand);color:#fff;font-size:12px;text-align:center;line-height:45px}
</style>
</head>
<body>

<div class="topbar">
  <div class="wrap">
    <div class="item">
      <svg width="15" height="15" viewBox="0 0 24 24"><path fill="#fff" d="M6.6 10.8a15 15 0 0 0 6.6 6.6l2.2-2.2c.3-.3.7-.4 1-.2 1.1.4 2.3.6 3.6.6.6 0 1 .4 1 1V20c0 .6-.4 1-1 1A17 17 0 0 1 3 4c0-.6.4-1 1-1h3.5c.6 0 1 .4 1 1 0 1.3.2 2.5.6 3.6.1.3 0 .7-.2 1z"/></svg>
      <span>123-456-7890</span>
    </div>
    <div class="item">
      <svg width="15" height="12" viewBox="0 0 24 18"><rect x="1" y="1" width="22" height="16" fill="#fff"/><path d="M1 1l11 9 11-9" stroke="#000" stroke-width="2" fill="none"/></svg>
      <span>info@northgaterealty.com</span>
    </div>
    <div class="login">
      <svg width="16" height="16" viewBox="0 0 24 24"><path fill="none" stroke="#fff" stroke-width="2" d="M14 3h6v18h-6M3 12h12M11 8l4 4-4 4"/></svg>
      Login
    </div>
  </div>
</div>

<header class="header">
  <div class="wrap">
    <div class="brand">
      <div class="name">NORTHGATE REALTY</div>
      <div class="sub">SERVICES</div>
    </div>
    <div class="weather">
      <div class="title">PERTH WEATHER</div>
      <div class="today">
        <svg width="34" height="34" viewBox="0 0 34 34"><circle cx="17" cy="17" r="8" fill="#f4b41a"/><g stroke="#f4b41a" stroke-width="2"><path d="M17 2v5M17 27v5M2 17h5M27 17h5M6 6l3.5 3.5M24.5 24.5L28 28M6 28l3.5-3.5M24.5 9.5L28 6"/></g></svg>
        <span class="temp">26°C</span>
        <span class="lbl"><b>Today</b><br>Cloudy</span>
      </div>
      <div class="days">
        <div class="day"><svg width="30" height="18" viewBox="0 0 30 18"><circle cx="10" cy="9" r="6" fill="#f4b41a"/><ellipse cx="19" cy="12" rx="10" ry="5" fill="#7fb6e6"/></svg>MON<br>18°-20°</div>
        <div class="day"><svg width="30" height="18" viewBox="0 0 30 18"><circle cx="15" cy="9" r="6" fill="#f4b41a"/></svg>TUE<br>28°-30°</div>
        <div class="day"><svg width="30" height="18" viewBox="0 0 30 18"><circle cx="10" cy="9" r="6" fill="#f4b41a"/><ellipse cx="19" cy="12" rx="10" ry="5" fill="#7fb6e6"/></svg>WED<br>20°-23°</div>
        <div class="day"><svg width="30" height="18" viewBox="0 0 30 18"><circle cx="15" cy="9" r="6" fill="#f4b41a"/></svg>THU<br>26°-31°</div>
      </div>
    </div>
  </div>
</header>

<nav class="nav">
  <div class="wrap">
    <ul>
      <li class="active">HOME</li><li>ABOUT US</li><li>SERVICES</li><li>FOR SALE</li><li>FOR RENT</li><li>TESTIMONIALS</li><li>CONTACT US</li>
    </ul>
  </div>
</nav>

<section class="hero">
  <div role="img" aria-label="Two property managers inspecting an apartment building, one holding a laptop" style="position:absolute;inset:0"></div>
  <div class="arrow-tab left"><svg width="16" height="20" viewBox="0 0 16 20"><path d="M12 2L4 10l8 8" stroke="#0355a3" stroke-width="3" fill="none"/></svg></div>
  <div class="arrow-tab right"><svg width="16" height="20" viewBox="0 0 16 20"><path d="M4 2l8 8-8 8" stroke="#0355a3" stroke-width="3" fill="none"/></svg></div>
  <div class="caption">We Are Professional Property Management Company Committed<br>To Take Care Of Your &nbsp;Property When It Is Vacant</div>
</section>

<section class="welcome">
  <div class="wrap">
    <h1 class="section-title">WELCOME TO NORTHGATE REALTY SERVICES</h1>
    <div class="divider"><svg width="20" height="20" viewBox="0 0 20 20" style="background:#fff"><path d="M3 10L10 4l7 6v7H3z" fill="#bbb"/></svg></div>
    <p>Lorem ipsum dolor sit amet, consectetuer adipiscing elit, sed diam nonummy nibh euismod tincidunt ut laoreet dolore magna aliquam erat volutpat. Ut wisi enim ad minim veniam, quis nostrud exerci tation ullamcorper suscipit lobortis nisl ut aliquip ex ea commodo consequat. Duis autem vel eum iriure dolor in hendrerit in vulputate velit esse molestie consequat, vel illum dolore eu feugiat nulla facilisis at vero eros et accumsan et iusto odio dignissim qui blandit praesent luptatum zzril delenit augue duis dolore te feugait nulla facilisi. <a>Read More..</a></p>
    <div class="callbox">
      <svg width="34" height="34" viewBox="0 0 34 34"><circle cx="17" cy="17" r="15" fill="none" stroke="#0355a3" stroke-width="2"/><path fill="#0355a3" d="M12 9c1-1 2 0 3 2s0 2-1 3c0 2 3 6 5 6 1-1 1-2 3-1s3 2 2 3c-2 3-6 2-9-1s-6-8-3-12z"/></svg>
      <span>Call Now &amp; Speak Directly - <strong>123 - 456 -7890</strong></span>
    </div>
  </div>
</section>

<section class="services">
  <div class="wrap">
    <h2 class="section-title">OUR SERVICES</h2>
    <div class="divider"><svg width="20" height="20" viewBox="0 0 20 20" style="background:#0355a3"><path d="M3 10L10 4l7 6v7H3z" fill="#9cc0e6"/></svg></div>
    <span class="svc-arrow" style="left:-20px">‹</span>
    <span class="svc-arrow" style="right:-20px">›</span>
    <div class="service-row">
      <div class="service">
        <div class="icon"><svg width="44" height="44" viewBox="0 0 44 44"><rect x="8" y="6" width="28" height="34" fill="#fff"/><g fill="#111"><rect x="12" y="10" width="5" height="5"/><rect x="20" y="10" width="5" height="5"/><rect x="28" y="10" width="5" height="5"/><rect x="12" y="19" width="5" height="5"/><rect x="20" y="19" width="5" height="5"/><rect x="28" y="19" width="5" height="5"/><rect x="12" y="28" width="5" height="5"/><rect x="28" y="28" width="5" height="5"/><rect x="19" y="30" width="7" height="10"/></g></svg></div>
        <h3>APARTMENT<br>MANAGEMENT</h3>
        <p>Lorem ipsum dolor sit amet sect<br>etmo adipiscing elit sed Lore</p>
        <div class="plus">+</div>
      </div>
      <div class="service">
        <div class="icon"><svg width="48" height="44" viewBox="0 0 48 44"><path d="M6 22L24 6l18 16" stroke="#fff" stroke-width="4" fill="none"/><rect x="12" y="21" width="24" height="17" fill="#fff"/><rect x="20" y="27" width="8" height="11" fill="#111"/><path d="M4 40L44 14" stroke="#fff" stroke-width="3"/></svg></div>
        <h3>FORECLOSURE<br>MANAGEMENT</h3>
        <p>Lorem ipsum dolor sit amet sect<br>etmo adipiscing elit sed Lore</p>
        <div class="plus">+</div>
      </div>
      <div class="service">
        <div class="icon"><svg width="48" height="44" viewBox="0 0 48 44"><path d="M4 22L24 5l20 17" stroke="#fff" stroke-width="4" fill="none"/><rect x="10" y="21" width="28" height="18" fill="#fff"/><rect x="14" y="26" width="20" height="6" fill="#111"/></svg></div>
        <h3>HOMEOWNER<br>ASSOCIATION</h3>
        <p>Lorem ipsum dolor sit amet sect<br>etmo adipiscing elit sed Lore</p>
        <div class="plus">+</div>
      </div>
      <div class="service">
        <div class="icon"><svg width="44" height="44" viewBox="0 0 44 44"><path d="M4 22L22 6l18 16" stroke="#fff" stroke-width="4" fill="none"/><rect x="10" y="21" width="24" height="18" fill="#fff"/><circle cx="22" cy="27" r="4" fill="#111"/><path d="M15 39c0-6 3-8 7-8s7 2 7 8z" fill="#111"/></svg></div>
        <h3>CONDOMINIUM<br>MANAGEMENT</h3>
        <p>Lorem ipsum dolor sit amet sect<br>etmo adipiscing elit sed Lore</p>
        <div class="plus">+</div>
      </div>
    </div>
  </div>
</section>

<section class="featured">
  <div class="wrap">
    <h2 class="section-title">FEATURED PROPERTIES</h2>
    <div class="divider"><svg width="20" height="20" viewBox="0 0 20 20" style="background:#fff"><path d="M3 10L10 4l7 6v7H3z" fill="#bbb"/></svg></div>
    <div class="cards">
      <div class="card">
        <div class="photo" role="img" aria-label="Brick family house with lawn" style="background:linear-gradient(180deg,#3f7fd0 0%,#8a4a3a 55%,#4f8a3a 100%)"></div>
        <h4>123 DOLLAR SMIT AMET</h4>
        <div class="desc">Lorem ipsum dolor sit amet, consecteti</div>
        <span class="tag">For Rent</span><span class="price">$ 123</span>
        <div class="stats"><div class="stat">⤢ 1200 sq ft</div><div class="stat">▭ 2 Beds</div><div class="stat">◔ 2 Baths</div></div>
      </div>
      <div class="card">
        <div class="photo" role="img" aria-label="Grey stone suburban house" style="background:linear-gradient(180deg,#a9c6e3 0%,#8b8e8f 55%,#5c7a45 100%)"></div>
        <h4>123 DOLLAR SMIT AMET</h4>
        <div class="desc">Lorem ipsum dolor sit amet, consecteti</div>
        <span class="tag">For Sell</span><span class="price">$ 123</span>
        <div class="stats"><div class="stat">⤢ 1200 sq ft</div><div class="stat">▭ 2 Beds</div><div class="stat">◔ 2 Baths</div></div>
      </div>
      <div class="card">
        <div class="photo" role="img" aria-label="Two-storey house with white picket fence" style="background:linear-gradient(180deg,#7fb0de 0%,#6b5a58 50%,#d9d9d9 80%,#5b8a3f 100%)"></div>
        <h4>123 DOLLAR SMIT AMET</h4>
        <div class="desc">Lorem ipsum dolor sit amet, consecteti</div>
        <span class="tag">For Rent</span><span class="price">$ 523</span>
        <div class="stats"><div class="stat">⤢ 1200 sq ft</div><div class="stat">▭ 2 Beds</div><div class="stat">◔ 2 Baths</div></div>
      </div>
      <div class="card">
        <div class="photo" role="img" aria-label="Modern white villa with lawn" style="background:linear-gradient(180deg,#c9d3db 0%,#ddd8cc 55%,#6c8f4a 100%)"></div>
        <h4>123 DOLLAR SMIT AMET</h4>
        <div class="desc">Lorem ipsum dolor sit amet, consecteti</div>
        <span class="tag">For Sell</span><span class="price">$ 320</span>
        <div class="stats"><div class="stat">⤢ 1200 sq ft</div><div class="stat">▭ 2 Beds</div><div class="stat">◔ 2 Baths</div></div>
      </div>
    </div>
  </div>
</section>

<section class="testimonials">
  <div class="wrap">
    <h2 class="section-title">CLIENT &nbsp;TESTIMONIALS</h2>
    <div class="divider"><svg width="20" height="20" viewBox="0 0 20 20" style="background:#efefef"><path d="M3 10L10 4l7 6v7H3z" fill="#bbb"/></svg></div>
    <div class="quote">
      <div class="avatar" role="img" aria-label="Client portrait"></div>
      <div>
        <p><b style="font-size:20px;color:#999">“</b> Lorem ipsdolor sit amet, consectetur adipiscing elit. Donec sit amet nulla vitae tortor iaculis commodo. Nulla interdum dui vitae lectus malesuada ac dignissim mi vehicula. Nullam ornare vulputate sem vitae convallis. Proin et faucibus eros. Nam id rutrum risus, quis eleifend tortor. Nulla scelerisque vitae ante vitae,rhoncus pellentesque turpis. Donec feugiat malesuada justo, quis porta urna egestas nec. Duis nec lobortis justo, ac varius ante. <b style="font-size:20px;color:#999">”</b></p>
        <div class="who">Mr. Daniel Hart</div>
      </div>
      <div class="rule"></div>
      <div class="nav-arrows">‹<span style="color:#0355a3">›</span></div>
    </div>
  </div>
</section>

<section class="newsletter">
  <div class="wrap">
    <div class="circle"><svg width="22" height="16" viewBox="0 0 22 16"><rect x="1" y="1" width="20" height="14" fill="#fff"/><path d="M1 1l10 8 10-8" stroke="#111" stroke-width="2" fill="none"/></svg></div>
    <h2>NEWSLETTER SIGNUP</h2>
    <svg class="chev" width="18" height="30" viewBox="0 0 18 30"><path d="M3 2l12 13L3 28" stroke="#fff" stroke-width="2" fill="none"/></svg>
    <div class="input">Your E-mail</div>
    <div class="btn">SIGN UP</div>
  </div>
</section>

<footer class="footer">
  <div class="wrap">
    <div class="fcol col-nav">
      <h5>NAVIGATION</h5>
      <ul><li>Home</li><li>About Us</li><li>Services</li><li>For Sale</li><li>For Rent</li><li>Testimonials</li><li>Contact Us</li></ul>
    </div>
    <div class="fcol col-links">
      <h5>OTHER LINKS</h5>
      <ul><li>Loren ipsum dolor</li><li>Dapibus eget eleme</li><li>Utm tellus dolor</li><li>Velmki cursu itas</li><li>Fir mnbvcd sirdcnc</li></ul>
    </div>
    <div class="fcol col-form">
      <h5>QUICK CONTACT</h5>
      <div class="field">Name</div>
      <div class="field">Email</div>
      <div class="field msg">Your message</div>
      <div class="submit">SUBMIT</div>
    </div>
    <div class="fcol col-touch">
      <h5>GET IN TOUCH</h5>
      <div class="touch"><div class="ic"><svg width="14" height="18" viewBox="0 0 14 18"><path d="M7 0a7 7 0 0 1 7 7c0 5-7 11-7 11S0 12 0 7a7 7 0 0 1 7-7z" fill="#fff"/><circle cx="7" cy="7" r="2.5" fill="#0355a3"/></svg></div><div><b>Northgate Realty Services</b><br>1234 Lren Ipsum dolor suit<br>Nbcdere, IL 1234</div></div>
      <div class="touch"><div class="ic"><svg width="16" height="16" viewBox="0 0 24 24"><path fill="#fff" d="M6.6 10.8a15 15 0 0 0 6.6 6.6l2.2-2.2c.3-.3.7-.4 1-.2 1.1.4 2.3.6 3.6.6.6 0 1 .4 1 1V20c0 .6-.4 1-1 1A17 17 0 0 1 3 4c0-.6.4-1 1-1h3.5c.6 0 1 .4 1 1 0 1.3.2 2.5.6 3.6.1.3 0 .7-.2 1z"/></svg></div><div>123-456-7890</div></div>
      <div class="touch"><div class="ic"><svg width="16" height="12" viewBox="0 0 22 16"><rect x="1" y="1" width="20" height="14" fill="#fff"/><path d="M1 1l10 8 10-8" stroke="#0355a3" stroke-width="2" fill="none"/></svg></div><div>info@northgaterealty.com</div></div>
    </div>
  </div>
</footer>

<div class="copyright">Copyright © 2016 Northgate Realty Services &nbsp;| &nbsp;All Rights Reserved.</div>

</body>
</html>
```